Commercial brochure presenting independent commercial activity

I would like to create a commercial brochure for my new professional activity.

This is a personal and not business oriented brochure because I will become an independent project assistant to assist engineering offices with one-off missions.

I want a 4 page A4 brochure

• Page 1: Logo, personal photo
• Page 2 and 3: Personal presentation and presentation of my activities
• Page4: contact information

My target audience: engineering offices and design offices

The objective of the brochure: it is to make my profile interesting so that design offices will want to use my services when there is demand

Sector of activity: food, chemical, pharmaceutical industry
The text of the brochure must remain in French and contain what is in the attached file

On page 1, you must keep a space for a photo of my profile which I will insert later because I do not have it yet and insert my monogram (it can be reworked to be inserted in the brochure)
The image with the logo (K/M) is the color range I want

engineering offices and design offices

industrie alimentaire, chimique, pharmaceutique

Sans Serif

0094D4
00A9DD
6FCCEA
C7EBF8
E9F6FB

• The plate must comply with current codes. Each reader must think that I am dynamic and that my services are of quality and equivalent to the presentation

```html
<!DOCTYPE html>
<html lang="fr">
<head>
<meta charset="UTF-8">
<title>Votre avantage – Assistant de projet indépendant</title>
<link rel="stylesheet" href="https://fonts.googleapis.com/css2?family=Montserrat:wght@300;400;500&display=swap">
<style>
  :root {
    --blue-deep: #0094D4;
    --blue: #00A9DD;
    --blue-band: #3A93D6;
    --blue-soft: #6FCCEA;
    --blue-pale: #C7EBF8;
    --blue-mist: #E9F6FB;
    --white: #FFFFFF;
    --text-blue: #1D8FD3;
  }
  * { box-sizing: border-box; margin: 0; padding: 0; }
  html, body { width: 848px; height: 1200px; overflow: hidden; background: var(--white); }
  body { font-family: "Montserrat", Arial, sans-serif; }

  .page { position: relative; width: 848px; height: 1200px; overflow: hidden; background: var(--white); }

  .side-panel {
    position: absolute; left: 0; top: 0; width: 296px; height: 304px;
    background: var(--blue);
  }
  .dot-row { position: absolute; display: flex; gap: 23px; }
  .dot-row span { width: 6px; height: 6px; border-radius: 50%; background: var(--blue-pale); }
  .dot-row--top { left: 50px; top: 24px; }
  .dot-row--bottom { left: 214px; top: 1168px; }
  .dot-row--bottom span { background: var(--blue-soft); }

  .section-title {
    position: absolute; left: 46px; top: 432px;
    transform: rotate(-90deg); transform-origin: left top;
    color: var(--white); font-weight: 300; font-size: 29px; letter-spacing: 4px;
    white-space: nowrap;
  }

  .advantages {
    position: absolute; left: 361px; top: 46px; width: 440px;
    color: var(--text-blue); font-size: 13.4px; line-height: 1.36;
  }
  .advantages p { margin-bottom: 14px; }

  .office-photo {
    position: absolute; left: 0; top: 304px; width: 848px; height: 568px;
    background:
      linear-gradient(180deg, rgba(255,255,255,0.35) 0%, rgba(255,255,255,0) 40%),
      linear-gradient(115deg, #3e4046 0%, #8b8f94 28%, #d9d2c6 50%, #efe8dc 62%, #9a8e80 82%, #4a4a4c 100%);
  }
  .photo-tint {
    position: absolute; left: 0; top: 304px; width: 296px; height: 568px;
    background: linear-gradient(180deg, rgba(0,169,221,0.9) 0%, rgba(0,169,221,0.35) 18%, rgba(0,169,221,0) 40%);
  }

  .asset-band {
    position: absolute; left: 191px; top: 818px; width: 657px; height: 54px;
    background: var(--blue-band);
    color: var(--white); font-size: 20px; font-weight: 400; letter-spacing: 0.5px;
    padding-left: 194px; line-height: 54px;
  }

  .offer-panel {
    position: absolute; left: 0; top: 872px; width: 296px; height: 328px;
    background: var(--blue); padding: 32px 20px 0 42px;
    color: var(--white); text-transform: uppercase;
    font-size: 18.2px; line-height: 1.3;
  }

  .quote-panel {
    position: absolute; left: 296px; top: 872px; width: 552px; height: 328px;
    background: var(--blue-mist);
  }
  .quote-text {
    position: absolute; left: 89px; top: 50px; width: 420px;
    color: var(--text-blue); font-size: 22px; line-height: 1.22; font-weight: 400;
  }
  .quote-mark { position: absolute; width: 30px; height: 26px; }
  .quote-mark--open { left: 45px; top: 56px; }
  .quote-mark--close { left: 500px; top: 238px; }
</style>
</head>
<body>
<main class="page">
  <div class="side-panel"></div>
  <div class="dot-row dot-row--top"><span></span><span></span><span></span><span></span><span></span></div>
  <h1 class="section-title">VOTRE AVANTAGE</h1>

  <section class="advantages">
    <p>Connaissance des besoins des concepteurs et des fabricants : J'ai travaillé des deux côtés, ce qui me permet de comprendre les défis et les attentes de chacun.</p>
    <p>Flexibilité : Je suis disponible pour des missions ponctuelles et à durée déterminée, sans engagement à long terme.</p>
    <p>Efficacité : Je peux vous aider à gérer les surcharges de travail et à respecter vos délais.</p>
    <p>Collaboration fluide : Je suis à votre disposition pour discuter de vos besoins et vous proposer des solutions sur mesure.</p>
  </section>

  <div class="office-photo" role="img" aria-label="Photo d'un bureau moderne lumineux avec grandes baies vitrées, postes de travail et salon"></div>
  <div class="photo-tint"></div>

  <div class="asset-band">A UNIQUE ASSET</div>

  <section class="offer-panel">
    J'offre mes services d'assistant de projet indépendant pour vous aider à gérer les pics de charge et les besoins spécifiques de votre bureau d'études. Mon expertise :
  </section>

  <section class="quote-panel">
    <svg class="quote-mark quote-mark--open" viewBox="0 0 30 26" aria-hidden="true">
      <path d="M12 2 C5 5 1 10 1 17 C1 22 4 25 8 25 C11 25 13 22 13 19 C13 16 11 14 8 14 C7 14 6 14 6 14 C6 10 9 6 13 4 Z M29 2 C22 5 18 10 18 17 C18 22 21 25 25 25 C28 25 30 22 30 19 C30 16 28 14 25 14 C24 14 23 14 23 14 C23 10 26 6 30 4 Z" fill="var(--text-blue)"/>
    </svg>
    <p class="quote-text">Malgré mon handicap en fauteuil roulant, je suis totalement opérationnel et mon expérience me permet de vous offrir une expertise de haut niveau. Je suis disponible à 35% dès septembre 2024 et je suis prêt à mettre mon expertise et mon dynamisme au service de votre succès.</p>
    <svg class="quote-mark quote-mark--close" viewBox="0 0 30 26" aria-hidden="true">
      <g transform="rotate(180 15 13)">
        <path d="M12 2 C5 5 1 10 1 17 C1 22 4 25 8 25 C11 25 13 22 13 19 C13 16 11 14 8 14 C7 14 6 14 6 14 C6 10 9 6 13 4 Z M29 2 C22 5 18 10 18 17 C18 22 21 25 25 25 C28 25 30 22 30 19 C30 16 28 14 25 14 C24 14 23 14 23 14 C23 10 26 6 30 4 Z" fill="var(--text-blue)"/>
      </g>
    </svg>
  </section>

  <div class="dot-row dot-row--bottom"><span></span><span></span><span></span><span></span><span></span><span></span></div>
</main>
</body>
</html>
```